Fernvale Activated Carbon (coal-based)

The packaging for granular activated carbon must have a simple industrial concept but looks classy. Industrial look, bold and credible, also eye catching. Weight: 25 kg

Target Market(s)

Industrial

Industry/Entity Type

Water Treatment Industry

Requirements
Must have
• Weight : 25 kg, must have "coal-based", warning symbol in packaging
Nice to have
• There is a picture of granular activated carbon (coal-based) on the package

```html
<!DOCTYPE html>
<html lang="en">
<head>
<meta charset="utf-8">
<title>Fernvale Activated Carbon – 25 kg Bag Layout</title>
<link rel="stylesheet" href="https://fonts.googleapis.com/css2?family=Montserrat:wght@800;900&family=Open+Sans:wght@400;600;700&family=Roboto+Condensed:wght@300;400&display=swap">
<style>
  :root {
    --backdrop: #f17a36;
    --bag-black: #000000;
    --brand-orange: #f26a24;
    --hex-light: #f89a32;
    --hex-grey: #555555;
    --ink-white: #ffffff;
    --ink-black: #000000;
  }
  html, body {
    margin: 0;
    padding: 0;
    width: 711px;
    height: 1200px;
    overflow: hidden;
    background: var(--backdrop);
  }
  .canvas {
    position: relative;
    width: 711px;
    height: 1200px;
  }
  .bag-layout {
    position: absolute;
    left: 25.5px;
    top: 330px;
    width: 660px;
    height: 540px;
  }
  .brand-name { font-family: "Montserrat", sans-serif; font-weight: 900; fill: var(--brand-orange); }
  .gusset-brand { font-family: "Montserrat", sans-serif; font-weight: 900; fill: var(--ink-black); }
  .product-line { font-family: "Montserrat", sans-serif; font-weight: 800; }
  .premium-tag { font-family: "Roboto Condensed", sans-serif; font-weight: 400; }
  .coal-based { font-family: "Open Sans", sans-serif; font-weight: 400; }
  .translations { font-family: "Roboto Condensed", sans-serif; font-weight: 300; fill: var(--ink-white); }
  .body-copy { font-family: "Open Sans", sans-serif; font-weight: 400; fill: var(--ink-white); }
  .label-bold { font-family: "Open Sans", sans-serif; font-weight: 700; fill: var(--ink-white); }
  .weight-label { font-family: "Open Sans", sans-serif; font-weight: 600; fill: var(--ink-black); }
</style>
</head>
<body>
<main class="canvas">
  <svg class="bag-layout" viewBox="0 0 1152 942" xmlns="http://www.w3.org/2000/svg">
    <defs>
      <linearGradient id="hex-orange-fade" x1="0" y1="0" x2="1" y2="1">
        <stop offset="0" stop-color="#f26a24" stop-opacity="0.15"/>
        <stop offset="0.5" stop-color="#f26a24"/>
        <stop offset="1" stop-color="#f7932f"/>
      </linearGradient>
      <linearGradient id="hex-light-fade" x1="0" y1="0" x2="0" y2="1">
        <stop offset="0" stop-color="#f89a32" stop-opacity="0.9"/>
        <stop offset="1" stop-color="#f26a24" stop-opacity="0.2"/>
      </linearGradient>
      <radialGradient id="hex-grey-fade" cx="0.5" cy="0.5" r="0.6">
        <stop offset="0" stop-color="#5a5a5a"/>
        <stop offset="1" stop-color="#000000"/>
      </radialGradient>
    </defs>

    <!-- Bag body -->
    <rect class="bag-surface" x="0" y="0" width="1152" height="942" fill="var(--bag-black)"/>

    <!-- Gusset bands -->
    <rect class="gusset-band" x="417" y="158" width="159" height="624" fill="var(--brand-orange)"/>
    <rect class="gusset-band" x="992" y="158" width="160" height="624" fill="var(--brand-orange)"/>

    <!-- Panel fold lines -->
    <g class="fold-lines" stroke="#1a1a1a" stroke-width="1">
      <line x1="417" y1="0" x2="417" y2="942"/>
      <line x1="576" y1="0" x2="576" y2="942"/>
      <line x1="992" y1="0" x2="992" y2="942"/>
      <line x1="0" y1="158" x2="417" y2="158"/>
    </g>

    <!-- BACK PANEL -->
    <g class="back-panel">
      <rect role="img" aria-label="Orange honeycomb hexagon cluster suggesting carbon granules" x="186" y="195" width="230" height="218" fill="url(#hex-orange-fade)" rx="6"/>
      <rect role="img" aria-label="Light orange honeycomb hexagons continuing onto the side gusset" x="417" y="195" width="159" height="220" fill="url(#hex-light-fade)"/>

      <text class="brand-name" x="82" y="442" font-size="43" textLength="254" lengthAdjust="spacingAndGlyphs">FERNVALE</text>

      <text class="coal-based" x="316" y="461" font-size="9" text-anchor="end" fill="var(--ink-white)">COAL-BASED</text>
      <rect class="premium-box" x="106" y="466" width="68" height="16" rx="2" fill="var(--brand-orange)"/>
      <text class="premium-tag" x="140" y="479" font-size="13" text-anchor="middle" fill="var(--ink-black)">PREMIUM</text>
      <text class="product-line" x="179" y="479" font-size="12.5" fill="var(--ink-white)" textLength="137" lengthAdjust="spacingAndGlyphs">ACTIVATED CARBON</text>

      <line x1="82" y1="517" x2="217" y2="517" stroke="var(--ink-white)" stroke-width="2"/>

      <g class="warning-header">
        <path d="M91 530 L100 545 L82 545 Z" fill="none" stroke="#e02020" stroke-width="2"/>
        <rect x="90" y="535" width="2" height="5" fill="var(--ink-white)"/>
        <rect x="90" y="541.5" width="2" height="2" fill="var(--ink-white)"/>
        <text class="label-bold" x="103" y="545" font-size="11">WARNING / CAUTION</text>
        <g class="hazard-diamonds" fill="none" stroke="var(--ink-white)" stroke-width="2">
          <path d="M238 526 L248 536 L238 546 L228 536 Z" stroke="#e02020"/>
          <path d="M238 530 L244 536 L238 542 L232 536 Z"/>
          <path d="M265 526 L275 536 L265 546 L255 536 Z" stroke="#e02020"/>
          <circle cx="265" cy="536" r="3.5"/>
        </g>
        <text class="body-copy" x="283" y="531" font-size="5.5">Harmful if inhaled.</text>
        <text class="body-copy" x="283" y="539" font-size="5.5">Eye irritant</text>
      </g>

      <g class="warning-copy body-copy" font-size="10.6">
        <text x="82" y="557" textLength="254" lengthAdjust="spacing">Activated carbon affects the respiratory and</text>
        <text x="82" y="572" textLength="254" lengthAdjust="spacing">cardiovascular system. Wet activated carbon can</text>
        <text x="82" y="587" textLength="254" lengthAdjust="spacing">deplete oxygen from the air creating dangerously</text>
        <text x="82" y="602" textLength="254" lengthAdjust="spacing">low levels of oxygen in confined spaces. Please pay</text>
        <text x="82" y="617">attention to working in confined spaces.</text>
      </g>

      <g class="handling-icons" fill="none" stroke="var(--ink-white)" stroke-width="1.6">
        <rect x="82" y="642" width="30" height="30" rx="3"/>
        <path d="M89 656 Q97 650 105 656 M97 652 L97 666 M91 663 Q97 668 103 663"/>
        <rect x="124" y="642" width="30" height="30" rx="3"/>
        <path d="M129 659 Q139 646 149 659 Z M139 659 L139 667 Q139 669 136 668"/>
        <rect x="166" y="642" width="30" height="30" rx="3"/>
        <circle cx="181" cy="657" r="4"/>
        <path d="M181 647 L181 650 M181 664 L181 667 M171 657 L174 657 M188 657 L191 657 M174 650 L176 652 M186 662 L188 664 M188 650 L186 652 M174 664 L176 662"/>
        <rect x="208" y="642" width="30" height="30" rx="3"/>
        <path d="M223 648 L223 666 M219 652 L227 652 M219 662 Q223 668 227 662"/>
        <rect x="250" y="642" width="30" height="30" rx="3"/>
        <path d="M265 649 L259 661 L271 661 Z M262 665 L268 665"/>
      </g>

      <text class="label-bold" x="82" y="701" font-size="7">BATCH NUMBER</text>
      <rect class="batch-field" x="82" y="709" width="109" height="23" rx="2" fill="var(--ink-white)"/>
    </g>

    <!-- GUSSET ONE -->
    <g class="gusset-left">
      <text class="gusset-brand" transform="translate(492,747) rotate(-90)" x="0" y="0" font-size="46" textLength="305" lengthAdjust="spacingAndGlyphs">FERNVALE</text>
      <g transform="translate(534,712) rotate(-90)">
        <rect x="0" y="-19" width="80" height="21" rx="3" fill="var(--ink-black)"/>
        <text class="premium-tag" x="40" y="-3" font-size="14" text-anchor="middle" fill="var(--brand-orange)">PREMIUM</text>
        <text class="product-line" x="85" y="-2" font-size="14" fill="var(--ink-black)" textLength="165" lengthAdjust="spacingAndGlyphs">ACTIVATED CARBON</text>
        <text class="coal-based" x="245" y="-19" font-size="9" text-anchor="end" fill="var(--ink-black)">COAL-BASED</text>
      </g>
    </g>

    <!-- FRONT PANEL -->
    <g class="front-panel">
      <rect role="img" aria-label="Grey honeycomb hexagon cluster" x="620" y="195" width="186" height="114" rx="8" fill="url(#hex-grey-fade)"/>

      <circle class="grade-badge" cx="931" cy="294" r="16" fill="none" stroke="var(--ink-white)" stroke-width="2"/>
      <text class="label-bold" x="931" y="321" font-size="6" text-anchor="middle">HIGH-GRADE</text>

      <text class="brand-name" x="619" y="387" font-size="56" textLength="330" lengthAdjust="spacingAndGlyphs">FERNVALE</text>

      <text class="coal-based" x="922" y="413" font-size="12" text-anchor="end" fill="var(--ink-white)">COAL-BASED</text>
      <rect class="premium-box" x="649" y="414" width="88" height="23" rx="2" fill="var(--brand-orange)"/>
      <text class="premium-tag" x="693" y="432" font-size="17" text-anchor="middle" fill="var(--ink-black)">PREMIUM</text>
      <text class="product-line" x="743" y="432" font-size="16.5" fill="var(--ink-white)" textLength="179" lengthAdjust="spacingAndGlyphs">ACTIVATED CARBON</text>

      <text class="translations" x="784" y="476" font-size="13" text-anchor="middle">活性炭  |  Активированный уголь  |  كربون مفعل</text>
      <text class="translations" x="784" y="498" font-size="13" text-anchor="middle">Charbon actif  |  Geactiveerde koolstof</text>

      <rect role="img" aria-label="Orange honeycomb hexagon cluster suggesting carbon granules" x="779" y="540" width="213" height="150" rx="8" fill="url(#hex-orange-fade)"/>
      <rect role="img" aria-label="Light orange honeycomb hexagons continuing onto the side gusset" x="992" y="530" width="160" height="165" fill="url(#hex-light-fade)"/>

      <polygon class="weight-hex" points="914,666 950,684 950,722 914,740 878,722 878,684" fill="var(--brand-orange)"/>
      <text class="weight-label" x="914" y="700" font-size="11" text-anchor="middle" font-weight="400">Weight</text>
      <text class="weight-label" x="914" y="715" font-size="11" text-anchor="middle">25Kg</text>

      <g class="usage-notes body-copy" font-size="7.6">
        <text x="619" y="709">ORDERS AND IMPURITIES*</text>
        <text x="619" y="720">FOR SPARKLING CLEAN WATER</text>
        <text x="619" y="731">IDEAL FOR ALL AQUARIUM FILTERS</text>
      </g>
    </g>

    <!-- GUSSET TWO -->
    <g class="gusset-right">
      <text class="gusset-brand" transform="translate(1068,502) rotate(-90)" x="0" y="0" font-size="47" textLength="310" lengthAdjust="spacingAndGlyphs">FERNVALE</text>
      <g transform="translate(1117,472) rotate(-90)">
        <rect x="0" y="-20" width="85" height="22" rx="3" fill="var(--ink-black)"/>
        <text class="premium-tag" x="42.5" y="-3" font-size="15" text-anchor="middle" fill="var(--brand-orange)">PREMIUM</text>
        <text class="product-line" x="90" y="-2" font-size="15" fill="var(--ink-black)" textLength="190" lengthAdjust="spacingAndGlyphs">ACTIVATED CARBON</text>
        <text class="coal-based" x="274" y="-20" font-size="10" text-anchor="end" fill="var(--ink-black)">COAL-BASED</text>
      </g>
    </g>
  </svg>
</main>
</body>
</html>
```